Emerging Ed-Tech Startup seeking Stationery Designs!

We are in need of basic set of stationery designs to be used for our business operations, letters, emails, and in-office materials. We are a technology startup enhancing on campus work experience offerings by establishing a collaborative work environment for the completion of such tasks.

Our colors are Vibrant Tiffany Blue/Black/White.

Website: www.scholarhorizonhub.com (Still under construction aside from the landing pages)

Please make sure the designs use a brighter more vibrant tiffany blue color than seen in the image files uploaded. We are not using those materials.

Our logo has been added as a file as well, please use that for any designs (include that logo). Thank you.

```html
<!DOCTYPE html>
<html lang="en">
<head>
<meta charset="utf-8">
<title>Scholar Horizon Hub – Stationery Set</title>
<link href="https://fonts.googleapis.com/css2?family=Jost:wght@400;500;600&family=Arimo&display=swap" rel="stylesheet">
<style>
  :root {
    --tiffany: #0fe6ea;
    --ink: #111111;
    --paper: #ffffff;
    --rule: #333333;
    --backdrop: #93663f;
    --faint: #e6f4f6;
    --label: #ffffff;
  }
  * { box-sizing: border-box; margin: 0; padding: 0; }
  html, body { width: 1200px; height: 700px; overflow: hidden; }
  body {
    position: relative;
    background: var(--backdrop);
    font-family: "Jost", sans-serif;
    color: var(--ink);
  }
  .sheet {
    position: absolute;
    background: var(--paper);
    box-shadow: 3px 3px 0 var(--ink);
    overflow: hidden;
  }
  .brand-name {
    position: absolute;
    font-family: "Jost", sans-serif;
    font-weight: 600;
    color: var(--ink);
    text-transform: uppercase;
    line-height: 1.05;
    letter-spacing: 0.3px;
  }
  .band {
    position: absolute;
    left: 0; right: 0;
    background: var(--tiffany);
    display: flex;
    align-items: center;
    justify-content: center;
    gap: 10px;
    font-size: 7px;
    font-weight: 500;
    letter-spacing: 0.4px;
  }
  .band span, .contact span { display: inline-flex; align-items: center; gap: 3px; }
  .icon { width: 7px; height: 7px; }
  .address {
    position: absolute;
    left: 0; right: 0;
    text-align: center;
    font-size: 7px;
    letter-spacing: 0.6px;
  }
  .watermark {
    position: absolute;
    font-weight: 600;
    color: var(--faint);
    text-transform: uppercase;
    text-align: center;
    line-height: 1;
  }

  /* Letterhead */
  .letterhead { left: 70px; top: 48px; width: 327px; height: 420px; }
  .letterhead .brand-name { left: 0; right: 0; top: 14px; text-align: center; font-size: 14px; }
  .letterhead .watermark { left: 60px; top: 150px; width: 200px; font-size: 44px; }
  .letterhead .band { top: 382px; height: 20px; }
  .letterhead .address { top: 406px; }

  /* Fax sheet */
  .fax { left: 432px; top: 48px; width: 328px; height: 420px; }
  .fax .brand-name { left: 24px; top: 14px; font-size: 13px; }
  .fax .contact {
    position: absolute; left: 226px; top: 22px;
    border-left: 1px solid #999; padding-left: 4px;
    display: flex; flex-direction: column; gap: 4px;
    font-size: 6.5px;
  }
  .fax-title {
    position: absolute; left: 25px; top: 88px;
    font-family: "Arimo", sans-serif; font-size: 21px;
  }
  .fax-fields { position: absolute; left: 28px; top: 132px; width: 272px; }
  .fax-row {
    display: flex; height: 38.7px; align-items: flex-start;
    border-bottom: 1.5px solid var(--rule);
    padding-top: 1px;
    font-family: "Arimo", sans-serif; font-size: 8px;
  }
  .fax-row .field { width: 176px; }
  .fax .band { top: 382px; height: 20px; }

  /* Envelopes */
  .envelope { left: 779px; width: 365px; height: 157px; }
  .envelope .flap {
    position: absolute; left: 0; right: 0; top: 0; height: 55px;
    display: flex; align-items: center; justify-content: center;
  }
  .envelope .flap .brand-name { position: static; font-size: 13px; }
  .envelope-white { top: 46px; }
  .envelope-white .flap { border-bottom: 1px solid var(--rule); }
  .envelope-black { top: 223px; }
  .envelope-black .flap { background: var(--ink); }
  .envelope-black .flap .brand-name { color: var(--paper); }
  .envelope-tiffany { top: 396px; }
  .envelope-tiffany .flap { background: var(--tiffany); }
  .envelope-tiffany .flap .brand-name { color: var(--paper); }

  /* Email signature */
  .signature { left: 65px; top: 500px; width: 347px; height: 92px; }
  .signature .brand-name { left: 12px; top: 9px; font-size: 10px; }
  .signature .person {
    position: absolute; right: 14px; top: 13px; text-align: right;
    font-size: 8px; font-weight: 500; letter-spacing: 0.5px; line-height: 1.9;
  }
  .signature .band { top: 59px; height: 16px; justify-content: flex-start; padding-left: 10px; font-size: 6.5px; }
  .signature .address { top: 80px; left: 10px; text-align: left; font-size: 6.5px; display: flex; align-items: center; gap: 3px; }
  .caption {
    position: absolute; left: 170px; top: 608px;
    font-size: 18px; color: var(--label); letter-spacing: 0.3px;
  }

  /* Business card */
  .card { left: 469px; top: 493px; width: 365px; height: 155px; }
  .card .brand-name { left: 15px; top: 14px; font-size: 13px; }
  .card .watermark { right: 12px; top: 72px; font-size: 18px; }
  .card .band { top: 120px; height: 17px; justify-content: flex-start; padding-left: 15px; font-size: 6.5px; }
  .card .web { position: absolute; left: 15px; top: 141px; font-size: 7px; letter-spacing: 0.8px; }
</style>
</head>
<body>

  <section class="sheet letterhead">
    <div class="brand-name">Scholar<br>Horizon Hub</div>
    <div class="watermark">Scholar<br>Horizon<br>Hub</div>
    <div class="band">
      <span><svg class="icon" viewBox="0 0 10 10"><path d="M2 1l2 2-1 1.5a6 6 0 0 0 2.5 2.5L7 6l2 2-1.5 1.5C4 9 1 6 .5 2.5z" fill="currentColor"/></svg>+91 20 5550142</span>
      <span><svg class="icon" viewBox="0 0 10 10"><circle cx="5" cy="5" r="4" fill="none" stroke="currentColor"/><path d="M1 5h8M5 1c-2 2.5-2 5.5 0 8M5 1c2 2.5 2 5.5 0 8" fill="none" stroke="currentColor" stroke-width=".7"/></svg>www.scholarhorizonhub.com</span>
    </div>
    <div class="address">Suite#B-14 Lake Road</div>
  </section>

  <section class="sheet fax">
    <div class="brand-name">Scholar<br>Horizon Hub</div>
    <div class="contact">
      <span><svg class="icon" viewBox="0 0 10 10"><path d="M2 1l2 2-1 1.5a6 6 0 0 0 2.5 2.5L7 6l2 2-1.5 1.5C4 9 1 6 .5 2.5z" fill="currentColor"/></svg>+91 20 5550142</span>
      <span><svg class="icon" viewBox="0 0 10 10"><circle cx="5" cy="5" r="4" fill="currentColor"/></svg>www.scholarhorizonhub.com</span>
    </div>
    <h1 class="fax-title">FAX</h1>
    <div class="fax-fields">
      <div class="fax-row"><span class="field">To</span><span class="field">From</span></div>
      <div class="fax-row"><span class="field">Fax</span><span class="field">Pages</span></div>
      <div class="fax-row"><span class="field">Phone</span><span class="field">Date</span></div>
      <div class="fax-row"><span class="field">Re</span><span class="field">CC</span></div>
    </div>
    <div class="band">Suite#B-14 Lake Road</div>
  </section>

  <section class="sheet envelope envelope-white">
    <div class="flap"><div class="brand-name">Scholar Horizon Hub</div></div>
  </section>
  <section class="sheet envelope envelope-black">
    <div class="flap"><div class="brand-name">Scholar Horizon Hub</div></div>
  </section>
  <section class="sheet envelope envelope-tiffany">
    <div class="flap"><div class="brand-name">Scholar Horizon Hub</div></div>
  </section>

  <section class="sheet signature">
    <div class="brand-name">Scholar<br>Horizon Hub</div>
    <div class="person">MS. CLARA BENNET<br>MARKETING MANAGER</div>
    <div class="band">
      <span><svg class="icon" viewBox="0 0 10 10"><path d="M2 1l2 2-1 1.5a6 6 0 0 0 2.5 2.5L7 6l2 2-1.5 1.5C4 9 1 6 .5 2.5z" fill="currentColor"/></svg>+91 20 5550142</span>
      <span><svg class="icon" viewBox="0 0 10 10"><rect x="3" y="1" width="4" height="8" rx="1" fill="none" stroke="currentColor"/></svg>+91 20 5550187</span>
      <span><svg class="icon" viewBox="0 0 10 10"><circle cx="5" cy="5" r="4" fill="currentColor"/></svg>www.scholarhorizonhub.com</span>
    </div>
    <div class="address"><svg class="icon" viewBox="0 0 10 10"><path d="M5 1L1 5h1.5v4h5V5H9z" fill="currentColor"/></svg>Suite#B-14 Lake Road</div>
  </section>
  <p class="caption">Email Signtaure</p>

  <section class="sheet card">
    <div class="brand-name">Scholar<br>Horizon Hub</div>
    <div class="watermark">Scholar<br>Horizon Hub</div>
    <div class="band">Suite#B-14 Lake Road</div>
    <div class="web">www.scholarhorizonhub.com</div>
  </section>

</body>
</html>
```